Webdesign for a Bikeshop in Innsbruck (submitted designs will be used for Masterthesis anonymously)

To obtain my master's degree, I am conducting a study in the field of web design as part of my master thesis. All submitted designs will therefore be used for study purposes. In order to achieve a homogeneous group, I would like to encourage not only male but also female web designers to submit a design. All submitted designs will be used anonymously for the study and therefore do not allow any conclusions to be drawn about your person. Since this is a contest, the winner will be chosen randomly from all serious submissions. I would be really happy if you would support me in my study. I think the results could be very informative and also useful for your further work (I won't go into more detail here as it could skew the results - but once the contest is over, feel free to contact me. Of course I will also provide you with my results as soon as my work is finished). Below you will find a usecase and a description of what the website should include:

The company Bikeshop Morvalt is planning to relaunch its own website and would like to present itself primarily as a competent and leading consultant in the field of cargo bikes. The design should appeal to a broad audience and embody an urban lifestyle. In any case, the website should include a landing page, a product overview page and a product details page, also make sure to design as gender neutral as possible. You only design the website. So don't worry about hardware or software limitations, just create the best bike store design you can.

1 page

• landing page, product overview page, product details page
• onlineshop

```html
<!DOCTYPE html>
<html lang="en">
<head>
<meta charset="utf-8">
<title>Bikeshop Morvalt – Cargo Bikes</title>
<link href="https://fonts.googleapis.com/css2?family=Roboto:wght@500;700;900&family=Open+Sans:wght@400;600&display=swap" rel="stylesheet">
<style>
:root{
  --accent:#4dc6e6;
  --dark:#1a1a1a;
  --ink:#111;
  --muted:#888;
  --soft:#f2f2f2;
  --line:#e6e6e6;
  --white:#fff;
  --footer:#0f0f0f;
  --bike-black:#2a2a2a;
  --bike-red:#b8322a;
  --bike-grey:#6e7274;
  --bike-wicker:#9a6b3a;
}
*{box-sizing:border-box;margin:0;padding:0}
html,body{width:1200px;height:4044px;overflow:hidden}
body{position:relative;font-family:"Open Sans",sans-serif;color:var(--ink);background:var(--white)}
.abs{position:absolute}
h1,h2,h3,.num{font-family:"Roboto",sans-serif}
.btn{position:absolute;display:flex;align-items:center;justify-content:center;font-size:14px;font-weight:600;border-radius:4px}
.btn-accent{background:var(--accent);color:var(--white)}
.pill{border-radius:24px}
.bar{position:absolute;width:50px;height:3px;background:var(--accent)}

/* nav */
.nav{left:0;top:0;width:1200px;height:63px;background:var(--white);display:flex;align-items:center;padding:0 40px;box-shadow:0 1px 4px rgba(0,0,0,.06)}
.brand{font-family:"Roboto",sans-serif;font-weight:700;font-size:24px;color:var(--accent)}
.menu{margin-left:auto;display:flex;gap:26px;font-size:14px}
.menu .on{color:var(--accent)}
.social{display:flex;gap:10px;margin-left:30px}
.social span{width:28px;height:28px;border-radius:50%;background:#f1f4f6;display:block;position:relative}
.social span::after{content:"";position:absolute;left:10px;top:10px;width:8px;height:8px;border-radius:50%;background:var(--accent)}

/* hero */
.hero{left:0;top:63px;width:1200px;height:637px;background:linear-gradient(180deg,#5b5048 0%,#4a4440 45%,#3a3836 100%)}
.hero-shade{left:0;top:0;width:100%;height:100%;background:rgba(0,0,0,.35)}
.hero h1{left:0;top:180px;width:1200px;text-align:center;color:var(--white);font-size:56px;line-height:64px;font-weight:900}
.hero p{left:0;top:330px;width:1200px;text-align:center;color:var(--white);font-size:17px;line-height:25px}
.hero .b1{left:435px;top:408px;width:148px;height:47px}
.hero .b2{left:601px;top:408px;width:151px;height:47px;background:var(--white);color:var(--ink)}
.arrow{top:574px;width:36px;height:36px;border:2px solid var(--white);border-radius:50%}
.dots{left:571px;top:587px;display:flex;gap:8px}
.dots span{width:11px;height:11px;border-radius:50%;border:2px solid var(--white)}
.dots .on{background:var(--accent);border-color:var(--accent)}

/* features */
.feat{top:781px;width:340px;height:287px;background:var(--dark);color:var(--white);padding:0 40px}
.feat .ico{position:absolute;left:40px;top:57px;width:48px;height:48px;border-radius:50%;background:#2b2b2b;border:2px solid var(--accent)}
.feat .num{position:absolute;right:40px;top:42px;font-size:66px;font-weight:900;color:#050505}
.feat h3{position:absolute;left:40px;top:140px;font-size:16px;font-weight:700}
.feat p{position:absolute;left:40px;top:185px;width:260px;font-size:13px;line-height:20px;color:#ccc}

/* about */
.about-img{left:0;top:1148px;width:600px;height:377px;background:linear-gradient(135deg,#6b6358,#3b3e40 60%,#7a7f80)}
.about{left:600px;top:1148px;width:600px;height:377px;background:var(--soft)}
.sec-title{font-size:40px;font-weight:900}
.txt{font-size:13px;line-height:20px;color:var(--muted)}

/* match */
.match h2{left:0;top:1562px;width:1200px;text-align:center;font-size:40px;font-weight:900}
.tabs{left:342px;top:1655px;display:flex;gap:8px;font-size:13px}
.tabs span{height:33px;padding:0 13px;display:flex;align-items:center;border-radius:3px}
.tabs .on{background:var(--accent);color:var(--white)}
.bike{top:1775px;width:230px;height:225px}
.bike-black{background:radial-gradient(ellipse 60% 42% at 50% 55%,var(--bike-black) 0%,#6a5a48 38%,rgba(255,255,255,0) 100%)}
.bike-red{background:radial-gradient(ellipse 60% 40% at 50% 55%,var(--bike-red) 0%,#5a3a36 40%,rgba(255,255,255,0) 100%)}
.bike-grey{background:radial-gradient(ellipse 60% 40% at 50% 52%,var(--bike-grey) 0%,#3a3a3a 40%,rgba(255,255,255,0) 100%)}
.bike-longtail{background:radial-gradient(ellipse 58% 36% at 50% 50%,var(--bike-red) 0%,#2a2a2a 42%,rgba(255,255,255,0) 100%)}

/* quote */
.quote-img{left:50px;top:2047px;width:550px;height:557px;background:linear-gradient(160deg,#8a7a4a,#6b4a32 50%,#4a5a6a)}
.quote{left:600px;top:2047px;width:600px;height:557px;background:var(--soft)}
.field{position:absolute;background:var(--white);border:1px solid #eee;font-size:13px;color:#777;padding:0 10px;display:flex;align-items:center}

/* news */
.news h2{left:0;top:2640px;width:1200px;text-align:center;font-size:40px;font-weight:900}
.card{top:2760px;width:300px;height:421px;border:1px solid var(--line);background:var(--white)}
.card .pic{position:absolute;left:17px;top:17px;width:266px;height:149px;background:linear-gradient(135deg,#7a6a5a,#4a4a4a)}
.card h3{position:absolute;left:17px;top:180px;width:266px;font-size:20px;line-height:23px;font-weight:700}
.card p{position:absolute;left:17px;top:264px;width:266px;font-size:11px;line-height:17px;color:var(--muted)}
.card .btn{left:17px;top:373px;width:266px;height:29px;border-radius:0;font-size:13px}

/* testimonial */
.testi h2{left:0;top:3279px;width:1200px;text-align:center;font-size:40px;font-weight:900}
.avatar{border-radius:50%;background:linear-gradient(135deg,#d8d0c6,#a79e95)}
.testi p{left:320px;top:3472px;width:560px;text-align:center;font-size:17px;line-height:25px;color:var(--muted)}

/* footer */
.footer{left:0;top:3650px;width:1200px;height:394px;background:var(--footer);color:var(--white)}
.fcol{top:90px;width:260px;font-size:13px}
.fcol h4{font-family:"Roboto",sans-serif;font-size:17px;font-weight:700;color:#888;margin-bottom:20px}
.fcol li{list-style:none;line-height:26px;display:flex;align-items:center;gap:8px}
.chev{color:var(--white);font-size:13px}
.ring{width:30px;height:30px;border:1px solid var(--white);border-radius:50%;display:inline-block;margin-right:6px}
.mail{margin-top:16px;width:240px;height:48px;border:1px solid var(--white);border-radius:3px;position:relative;font-size:13px;color:#aaa;padding:15px 18px}
.mail span{position:absolute;right:6px;top:8px;height:30px;width:90px;background:var(--accent);color:var(--white);border-radius:3px;display:flex;align-items:center;justify-content:center}
.copy{left:60px;top:358px;font-size:13px;color:#ccc}
.copy u{color:var(--accent)}
.totop{left:1123px;top:330px;width:40px;height:40px;border-radius:50%;background:var(--accent)}
</style>
</head>
<body>

<header class="abs nav">
  <div class="brand">Bikeshop Morvalt</div>
  <nav class="menu"><span class="on">Home</span><span>About</span><span>Product Overview</span><span>Product Details</span><span>Pages ▾</span><span>Contact</span></nav>
  <div class="social" aria-label="Social links"><span></span><span></span><span></span><span></span></div>
</header>

<section class="abs hero">
  <div class="abs hero-shade" role="img" aria-label="Photo: rider on a red electric cargo bike in a town square"></div>
  <h1 class="abs">The Truely Heavy Duty<br>Electric Cargo Bikes</h1>
  <p class="abs">Vero elitr justo clita lorem. Ipsum dolor at sed stet sit diam no. Kasd rebum ipsum et diam<br>justo clita et kasd rebum sea elitr.</p>
  <div class="btn btn-accent pill b1">Read More</div>
  <div class="btn pill b2">Free Quote</div>
  <svg class="abs arrow" style="left:517px" viewBox="0 0 36 36"><path d="M20 12l-6 6 6 6" fill="none" stroke="#fff" stroke-width="2"/></svg>
  <div class="abs dots"><span class="on"></span><span></span><span></span></div>
  <svg class="abs arrow" style="left:646px" viewBox="0 0 36 36"><path d="M16 12l6 6-6 6" fill="none" stroke="#fff" stroke-width="2"/></svg>
</section>

<div class="abs feat" style="left:69px"><div class="ico"></div><div class="num">01</div><h3>5 Year Warrenty</h3><p>Vero elitr justo clita lorem ipsum dolor at sed stet sit diam rebum ipsum et diam justo clita et</p></div>
<div class="abs feat" style="left:430px"><div class="ico"></div><div class="num">02</div><h3>Free Delivery</h3><p>Vero elitr justo clita lorem ipsum dolor at sed stet sit diam rebum ipsum et diam justo clita et</p></div>
<div class="abs feat" style="left:790px"><div class="ico"></div><div class="num">03</div><h3>24/7 Support</h3><p>Vero elitr justo clita lorem ipsum dolor at sed stet sit diam rebum ipsum et diam justo clita et</p></div>

<div class="abs about-img" role="img" aria-label="Photo: two riders in covered electric cargo vehicles"></div>
<section class="abs about">
  <div class="bar" style="left:40px;top:80px"></div>
  <h2 class="abs sec-title" style="left:40px;top:94px">About Us</h2>
  <p class="abs txt" style="left:40px;top:162px;width:510px">Tempor erat elitr rebum at clita. Diam dolor diam ipsum sit. Aliqu diam amet diam et eos. Clita erat ipsum et lorem et sit, sed stet lorem sit clita duo justo erat amet</p>
  <div class="btn btn-accent pill" style="left:40px;top:250px;width:166px;height:47px">Explore More</div>
</section>

<section class="match">
  <h2 class="abs">Find Your Perfect Match</h2>
  <div class="abs tabs"><span class="on">Utility Bikes</span><span>Cycle Trucks</span><span>Longtails</span><span>Cargo Tricycles</span><span>E-Cargo Bikes</span></div>
  <div class="abs bike bike-black" style="left:69px" role="img" aria-label="Product photo: black utility bike with a wicker front basket"></div>
  <div class="abs bike bike-red" style="left:345px" role="img" aria-label="Product photo: red utility bike with a black front crate"></div>
  <div class="abs bike bike-grey" style="left:620px" role="img" aria-label="Product photo: grey bike with front and rear cargo boxes"></div>
  <div class="abs bike bike-longtail" style="left:896px" role="img" aria-label="Product photo: red electric longtail bike with side bags"></div>
</section>

<div class="abs quote-img" role="img" aria-label="Photo: woman with an e-bike on a wooden bridge"></div>
<section class="abs quote">
  <div class="bar" style="left:40px;top:80px"></div>
  <h2 class="abs sec-title" style="left:40px;top:94px">Free Quote</h2>
  <p class="abs txt" style="left:40px;top:184px;width:515px">Tempor erat elitr rebum at clita. Diam dolor diam ipsum sit. Aliqu diam amet diam et eos. Clita erat ipsum et lorem et sit, sed stet lorem sit clita duo justo erat amet</p>
  <div class="field" style="left:40px;top:249px;width:247px;height:44px">Your Name</div>
  <div class="field" style="left:302px;top:249px;width:248px;height:44px">Your Email</div>
  <div class="field" style="left:40px;top:309px;width:247px;height:44px">Your Mobile</div>
  <div class="field" style="left:302px;top:309px;width:248px;height:44px">Select Your Query<span style="margin-left:auto">⌄</span></div>
  <div class="field" style="left:40px;top:369px;width:510px;height:47px;align-items:flex-start;padding-top:6px">Massage</div>
  <div class="btn btn-accent" style="left:40px;top:430px;width:510px;height:47px">Get A Free Quote</div>
</section>

<section class="news">
  <h2 class="abs">Recent News</h2>
  <article class="abs card" style="left:116px"><div class="pic" role="img" aria-label="Photo: parent riding a cargo bike with a child"></div><h3>Cycling as a Part of Daily Life: A Review of Health Perspectives</h3><p>Health aspects of day-to-day cycling have gained attention from the health sector aiming to increase levels of physical activity, and from the transport and planning sector, to justify investments in cycling.</p><div class="btn btn-accent">Read More</div></article>
  <article class="abs card" style="left:449px"><div class="pic" role="img" aria-label="Photo: bicycle parked on a city street"></div><h3>How car culture colonised our thinking – and our language</h3><p>When we block traffic from a street, like for a sports event or a street party, we say that the street is “closed”. But who is it closed for? For motorists. But really, that street is now open to people.</p><div class="btn btn-accent">Read More</div></article>
  <article class="abs card" style="left:782px"><div class="pic" role="img" aria-label="Photo: family riding a cargo bike"></div><h3>Why aren’t more big bike firms tracking their environmental impact?</h3><p>One of the world’s biggest bicycle brands recently released its sustainability report for 2021. Remarkably, this appears to be the first time a major bike company has published such a document.</p><div class="btn btn-accent">Read More</div></article>
</section>

<section class="testi">
  <div class="bar" style="left:575px;top:3261px"></div>
  <h2 class="abs">Testimonial</h2>
  <div class="abs avatar" style="left:500px;top:3380px;width:50px;height:50px" role="img" aria-label="Client portrait"></div>
  <div class="abs avatar" style="left:559px;top:3364px;width:82px;height:82px;border:3px solid var(--accent)" role="img" aria-label="Client portrait"></div>
  <div class="abs avatar" style="left:650px;top:3380px;width:50px;height:50px" role="img" aria-label="Client portrait"></div>
  <div class="abs" style="left:589px;top:3436px;width:22px;height:22px;border-radius:50%;background:var(--white);color:var(--accent);font:700 16px/24px Roboto,sans-serif;text-align:center">“</div>
  <p class="abs">Clita clita tempor justo dolor ipsum amet kasd amet duo justo duo duo labore sed sed. Magna ut diam sit et amet stet eos sed clita erat magna elitr erat sit sit erat at rebum justo sea clita.</p>
  <div class="abs" style="left:0;top:3560px;width:1200px;text-align:center;font:700 20px Roboto,sans-serif">Client Name</div>
  <div class="abs" style="left:0;top:3592px;width:1200px;text-align:center;font-size:13px;color:var(--accent)">Profession</div>
</section>

<footer class="abs footer">
  <div class="abs fcol" style="left:60px"><h4>Address</h4>
    <ul>
      <li><svg width="12" height="14" viewBox="0 0 12 14"><path d="M6 0a5 5 0 0 0-5 5c0 4 5 9 5 9s5-5 5-9a5 5 0 0 0-5-5zm0 7a2 2 0 1 1 0-4 2 2 0 0 1 0 4z" fill="#fff"/></svg>Morvalt, Austria</li>
      <li><svg width="13" height="13" viewBox="0 0 13 13"><path d="M3 0l2 3-1.5 1.5a8 8 0 0 0 5 5L10 8l3 2-1 3C5 13 0 8 0 1z" fill="#fff"/></svg>+012 345 67890</li>
      <li><svg width="14" height="11" viewBox="0 0 14 11"><rect width="14" height="11" rx="1" fill="#fff"/><path d="M0 1l7 5 7-5" fill="none" stroke="#0f0f0f"/></svg>info@example.com</li>
    </ul>
    <div style="margin-top:14px"><span class="ring"></span><span class="ring"></span><span class="ring"></span><span class="ring"></span></div>
  </div>
  <div class="abs fcol" style="left:339px"><h4>Services</h4><ul><li><span class="chev">›</span>Business Security</li><li><span class="chev">›</span>Fire Detection</li><li><span class="chev">›</span>Alarm Systems</li><li><span class="chev">›</span>CCTV &amp; Video</li><li><span class="chev">›</span>Smart Home</li></ul></div>
  <div class="abs fcol" style="left:620px"><h4>Quick Links</h4><ul><li><span class="chev">›</span>About Us</li><li><span class="chev">›</span>Contact Us</li><li><span class="chev">›</span>Our Services</li><li><span class="chev">›</span>Terms &amp; Condition</li><li><span class="chev">›</span>Support</li></ul></div>
  <div class="abs fcol" style="left:900px"><h4>Newsletter</h4><p style="line-height:20px">Dolor amet sit justo amet elitr clita ipsum elitr est.</p><div class="mail">Your email<span>Subscribe</span></div></div>
  <div class="abs copy">© <u>Home</u>, All Right Reserved.</div>
  <svg class="abs totop" viewBox="0 0 40 40"><path d="M20 28V13M14 19l6-6 6 6" fill="none" stroke="#fff" stroke-width="2"/></svg>
</footer>

</body>
</html>
```